Corvantis websites redesign

Www.cor-vantis.com needs to be redesigned along with updations. The incremental material will be provided for the updations. We are looking for complete redesign of the pages with the new content. The complete write up will be provided soon

Target Market(s)

Global

Coding

Coded - Design and coding required

Number of Pages Required

5+ page

Requirements
Must have
• A clean and slick design for the Consulting.
Should not have
• Too many pictures which reduces the speed of the site

```html
<!DOCTYPE html>
<html lang="en">
<head>
<meta charset="utf-8">
<title>Corvantis Consultancy</title>
<link href="https://fonts.googleapis.com/css2?family=Source+Sans+3:wght@400;600&display=swap" rel="stylesheet">
<style>
:root{
  --blue:#3aa8cf;
  --maroon:#5e1f22;
  --navy:#28354f;
  --ink:#222;
  --footer:#e6e6e6;
  --rule:#cfcfcf;
  --white:#fff;
}
*{margin:0;padding:0;box-sizing:border-box}
html,body{width:1106px;height:1200px;overflow:hidden;background:var(--white)}
body{position:relative;font-family:"Source Sans 3",sans-serif;color:var(--ink)}
.site-header{position:absolute;top:0;left:0;width:1106px;height:71px;background:var(--white)}
.brand{position:absolute;left:69px;top:16px;display:flex;align-items:center;gap:10px}
.brand-dot{width:36px;height:36px;border-radius:50%;background:var(--blue)}
.brand-name{font-size:31px;font-weight:400;color:var(--navy);line-height:1}
.main-nav{position:absolute;right:69px;top:0;height:71px;display:flex}
.main-nav a{display:flex;align-items:center;padding:0 20px;height:71px;font-size:12.5px;color:var(--ink);text-decoration:none;letter-spacing:.3px}
.main-nav a.active{background:var(--blue);color:var(--white);font-weight:600;padding:0 24px}
.hero{position:absolute;top:71px;left:0;width:1106px;height:413px;background:radial-gradient(ellipse at 50% 40%,#4a4a4c 0%,#262628 55%,#101011 100%)}
.hero-title{position:absolute;top:70px;left:0;width:100%;text-align:center;color:var(--white);font-size:35px;font-weight:600;line-height:42px;letter-spacing:.5px}
.hero-arrow{position:absolute;top:186px}
.hero-arrow.prev{left:56px}
.hero-arrow.next{right:56px}
.welcome{position:absolute;top:520px;left:69px;width:968px;text-align:center}
.welcome-title{display:flex;justify-content:center;align-items:center;gap:12px;font-size:21px;font-weight:600;color:var(--maroon)}
.welcome-dot{width:24px;height:24px;border-radius:50%;background:var(--blue)}
.welcome-text{margin-top:16px;font-size:13.3px;line-height:22px;color:var(--ink)}
.btn{position:absolute;top:683px;left:487px;width:131px;height:40px;background:var(--navy);color:var(--white);font-size:13.5px;font-weight:600;display:flex;align-items:center;justify-content:center;border-radius:2px}
.rule{position:absolute;top:750px;left:69px;width:968px;border-top:1px solid var(--rule)}
.service{position:absolute;top:783px;width:304px;height:234px;color:var(--white);text-align:center;border-radius:2px}
.service.consultancy{left:69px;background:var(--blue)}
.service.systems{left:401px;background:var(--maroon)}
.service.cases{left:733px;background:var(--navy)}
.service h2{margin-top:22px;font-size:19px;font-weight:600;letter-spacing:.5px}
.service-icon{width:88px;height:88px;border-radius:50%;background:var(--white);margin:12px auto 0;display:flex;align-items:center;justify-content:center}
.service p{margin-top:14px;font-size:13px;line-height:22px;padding:0 16px}
.service a{display:inline-block;margin-top:1px;font-size:13px;font-weight:600;color:var(--white)}
.site-footer{position:absolute;top:1062px;left:0;width:1106px;height:138px;background:var(--footer);text-align:center}
.footer-nav{margin-top:24px;display:flex;justify-content:center;gap:36px}
.footer-nav a{font-size:12px;color:var(--navy);text-decoration:none}
.footer-nav a.active{font-weight:600}
.copyright{margin-top:9px;font-size:12px;color:var(--ink)}
.social{margin-top:14px;display:flex;justify-content:center;gap:6px}
.social span{width:30px;height:30px;border:1.5px solid var(--navy);border-radius:50%}
</style>
</head>
<body>
<header class="site-header">
  <div class="brand"><span class="brand-dot"></span><span class="brand-name">Corvantis</span></div>
  <nav class="main-nav">
    <a class="active" href="#">HOME</a>
    <a href="#">FOUNDER</a>
    <a href="#">CONSULTANCY</a>
    <a href="#">SYSTEM</a>
    <a href="#">CASE STUDIES</a>
    <a href="#">CONTACT US</a>
  </nav>
</header>

<section class="hero" role="img" aria-label="Group of business professionals in suits standing with arms crossed in front of a dark world map">
  <h1 class="hero-title">WORLD MERCHANDISINGTRADE<br>2012 ( USD BILLION)</h1>
  <svg class="hero-arrow prev" width="20" height="40" viewBox="0 0 20 40"><polyline points="18,2 2,20 18,38" fill="none" stroke="#fff" stroke-width="2.5"/></svg>
  <svg class="hero-arrow next" width="20" height="40" viewBox="0 0 20 40"><polyline points="2,2 18,20 2,38" fill="none" stroke="#fff" stroke-width="2.5"/></svg>
</section>

<section class="welcome">
  <h2 class="welcome-title"><span class="welcome-dot"></span>WELCOME TO OUR WEBSITE</h2>
  <p class="welcome-text">Corvantis Consultancy Limited capitalizes on synergies arising from trade and investment linkages between countries and knowledge of traditional and non-traditional pools of liquidity to provide consultancy services to Emerging country banks, Corporates and SMEs. The Consultancy provides bank neutral views to Corporates and SMEs in Asian emerging markets and helps in improving financial structure and efficient use of funds. Our endeavor is to provide a distinct bottom line advantage to our clients.</p>
</section>
<a class="btn">READ MORE</a>
<div class="rule"></div>

<article class="service consultancy">
  <h2>CONSULTANCY</h2>
  <div class="service-icon">
    <svg width="56" height="40" viewBox="0 0 56 40" fill="#222">
      <circle cx="14" cy="10" r="7"/><circle cx="42" cy="10" r="7"/>
      <path d="M2 36c0-10 5-16 12-16s12 6 12 16z"/><path d="M30 36c0-10 5-16 12-16s12 6 12 16z"/>
      <circle cx="28" cy="12" r="8" stroke="#fff" stroke-width="2"/>
      <path d="M14 40c0-11 6-18 14-18s14 7 14 18z" stroke="#fff" stroke-width="2"/>
    </svg>
  </div>
  <p>Aliquam molestie, mi et imperdiet euismod, dui purus auctor tellus, et interdum..</p>
  <a href="#">LEARN MORE</a>
</article>

<article class="service systems">
  <h2>SYSTEMS</h2>
  <div class="service-icon">
    <svg width="56" height="44" viewBox="0 0 56 44" fill="none" stroke="#222" stroke-width="3">
      <circle cx="22" cy="14" r="8"/><circle cx="10" cy="30" r="5"/>
      <rect x="26" y="24" width="22" height="14"/><line x1="22" y1="41" x2="54" y2="41"/>
    </svg>
  </div>
  <p>Aliquam molestie, mi et imperdiet euismod, dui purus auctor tellus, et interdum..</p>
  <a href="#">LEARN MORE</a>
</article>

<article class="service cases">
  <h2>CASE STUDIES</h2>
  <div class="service-icon">
    <svg width="56" height="46" viewBox="0 0 56 46" fill="none" stroke="#222" stroke-width="2.5">
      <rect x="4" y="8" width="22" height="28"/><line x1="9" y1="16" x2="21" y2="16"/><line x1="9" y1="22" x2="21" y2="22"/><line x1="9" y1="28" x2="21" y2="28"/>
      <rect x="22" y="4" width="30" height="26" fill="#fff"/><rect x="26" y="8" width="22" height="8" fill="#222"/>
      <line x1="37" y1="30" x2="37" y2="40"/><line x1="29" y1="42" x2="45" y2="42"/>
    </svg>
  </div>
  <p>Aliquam molestie, mi et imperdiet euismod, dui purus auctor tellus, et interdum..</p>
  <a href="#">LEARN MORE</a>
</article>

<footer class="site-footer">
  <nav class="footer-nav">
    <a class="active" href="#">HOME</a>
    <a href="#">FOUNDER</a>
    <a href="#">CONSULTANCY</a>
    <a href="#">SYSTEM</a>
    <a href="#">CASE STUDIES</a>
    <a href="#">CONTACT US</a>
  </nav>
  <p class="copyright">Copyright © 2016 Corvantis Consultancy Limited</p>
  <div class="social"><span></span><span></span><span></span><span></span></div>
</footer>
</body>
</html>
```